IV Nutritional Clinic Web Design

We are working with Velmo. They are an IV Nutritional Clinic and in need of a new website design.
Some sites to use for inspiration:
https://brantlowcare.example
https://www.zolvarihealth.example
https://www.quellspa.example
https://pimrolift.example
https://www.dorvak-well.example/pages/iv-therapy-west-hollywood
https://www.tqoncowell.example/cancer-care/iv-drips/
https://drelmavita.example
https://salbrikmed.example
Thank you for taking the time to consider designing a website for us. We are web developers based in Stockton, CA, USA. Most of our projects go through the same process. Understanding this process may help you win a project with us. We custom-code all of our websites in-house. We don’t have any requirements as to what tools you use for your design, but we prefer Figma files. For any design that we label as four-stars, we send it to the client for review. The client picks the final design they want us to use. Once we complete this process, we will continue to show additional clients all the four-star sites and purchase them later. Your designs will have multiple chances to sell. For better chances of success, we ask that you follow these guidelines.
IMAGES:
If you use any images or icons in the design, we ask that you have a link to the asset so we can purchase the image/icon. Most of the designs we submit do not have the customer’s images on them unless they have some great images. Be creative; show us the feeling you are trying to portray with your image choices. Use any royalty-free site you choose. We subscribe to Corvix and mainly use their images, but we can purchase images outside of Corvix.
PLEASE NOTE: we will not submit designs to clients with watermarks on the images.
FONTS:
We ask that you identify the fonts used in the design. This can be done in a message if you want. We typically use Lumen Typeset and Corvix Fonts.
CONTENT:
We're always open to different content and ideas. We often submit designs with stock images so the client can see our vision. We typically take pictures after the website launch to use their images with our vision. Lorem Ipsum is fine for paragraphs, but we ask that you write the headers in correct English. We want to be able to show the vision and identify the sections of the website.
INSPIRATION:
We typically add a couple of links in the brief of websites we like to help you get started in your design.
REVISIONS:
We do not often ask for revisions of the designs unless we see something in the design that may not appeal to the client. If there are slight changes that we want to make, we do that in the development process.
FEEDBACK:
We rarely give feedback on designs during the design process. We are working on many website projects and do not have the time to provide feedback. We usually respond if your request is well thought out and asks specific questions, but a note asking “feedback, please” usually goes unanswered.
Number of Pages Required
1 page
Look and feel
Each slider illustrates characteristics of the customer's brand and the style your logo design should communicate.

```html
<!DOCTYPE html>
<html lang="en">
<head>
<meta charset="utf-8">
<title>Velmo – IV Nutrient Therapy</title>
<link href="https://fonts.googleapis.com/css2?family=Poppins:wght@400;500;600;700&display=swap" rel="stylesheet">
<style>
:root{
  --navy:#1e3a8f;
  --green:#8ab453;
  --ink:#2b2b2b;
  --muted:#7a7a7a;
  --mist:#eef4fa;
  --stage:#c8c8c8;
  --white:#ffffff;
}
*{box-sizing:border-box;margin:0;padding:0}
html,body{width:1200px;height:2473px;overflow:hidden}
body{background:var(--stage);font-family:'Poppins',sans-serif;color:var(--ink)}
.page{position:absolute;left:102px;top:84px;width:997px;height:2304px;background:var(--white);overflow:hidden;box-shadow:0 6px 24px rgba(0,0,0,.18)}
.abs{position:absolute}
.brand{font-weight:700;font-size:26px;letter-spacing:1px;color:var(--navy);line-height:1}
.nav a{position:absolute;font-size:9.5px;font-weight:500;color:var(--ink);text-decoration:none;line-height:12px}
.nav a.active{color:var(--green)}
.nav a.active::before{content:"";position:absolute;left:0;right:0;top:-6px;height:1.5px;background:var(--green)}
.icon-btn{position:absolute;width:22px;height:22px;border-radius:50%;background:var(--white);box-shadow:0 2px 6px rgba(0,0,0,.12);display:flex;align-items:center;justify-content:center}

/* photo placeholders: soft tonal gradients in each scene's main colours */
.photo{display:block}
.ph-infusion{background:radial-gradient(circle at 68% 45%,#b8323a 0 14%,transparent 34%),radial-gradient(circle at 20% 30%,#8fb06a 0 10%,transparent 32%),linear-gradient(135deg,#c9b39c,#e6e1da 55%,#8a7d70)}
.ph-patient{background:radial-gradient(circle at 50% 30%,#2f5a5c 0 14%,transparent 30%),linear-gradient(180deg,#e9ecef,#f4f4f2 55%,#dcdfe2)}
.ph-nurse{background:radial-gradient(circle at 45% 25%,#f3f1ee 0 16%,transparent 32%),radial-gradient(circle at 35% 80%,#a52a34 0 5%,transparent 14%),linear-gradient(180deg,#ead5c4,#f1ece7 60%,#dfe7ee)}
.ph-consult{background:radial-gradient(circle at 20% 25%,#8a79c9 0 10%,transparent 30%),linear-gradient(135deg,#ddd6ef,#f4f2f6 50%,#e8e4ee)}
.ph-cannula{background:radial-gradient(circle at 55% 50%,#e2d14a 0 6%,transparent 18%),linear-gradient(135deg,#f2e8df,#ebe4de 50%,#d8cfc7)}
.ph-arm{background:radial-gradient(circle at 70% 75%,#2e8c50 0 5%,transparent 14%),linear-gradient(135deg,#eef0f2,#c9ccd1 55%,#9ea3aa)}
.ph-portrait-a{background:radial-gradient(circle at 50% 60%,#efefee 0 12%,transparent 24%),linear-gradient(180deg,#2f2b29,#4b4643 55%,#6a6561)}
.ph-portrait-b{background:radial-gradient(circle at 50% 85%,#c2474a 0 22%,transparent 42%),linear-gradient(180deg,#f0f0f0,#e0d8d4)}
.ph-portrait-c{background:radial-gradient(circle at 30% 40%,#5a3a2c 0 18%,transparent 38%),linear-gradient(180deg,#dcdcdc,#c9c4c0 60%,#3a3a3c)}
.ph-avatar{background:linear-gradient(135deg,#e2535f,#f3b1b7)}

.btn{position:absolute;background:var(--green);color:var(--white);font-size:8.5px;font-weight:600;border-radius:14px;display:flex;align-items:center;justify-content:center;letter-spacing:.3px}
.section-title{font-weight:700;font-size:21px;color:var(--ink);line-height:25px;white-space:nowrap}
.rule{position:absolute;display:flex;gap:6px}
.rule i{display:block;width:34px;height:2px;background:var(--green)}
.rule i+i{background:var(--navy)}
.band{position:absolute;left:0;width:997px;background:var(--mist)}
.svc-card{position:absolute;top:848px;width:216px;height:204px;background:var(--white);border-radius:6px;overflow:hidden}
.svc-card .photo{height:133px}
.svc-card .glyph{position:absolute;left:27px;top:150px;width:40px;height:40px}
.svc-card h3{position:absolute;left:82px;top:154px;font-size:12px;font-weight:600;line-height:16px}
.arrow{position:absolute;width:19px;height:19px;border:1.5px solid var(--green);border-radius:50%;display:flex;align-items:center;justify-content:center}
.review{position:absolute;left:160px;top:1277px;width:319px;height:176px;background:var(--white);border-radius:4px;box-shadow:0 4px 16px rgba(0,0,0,.12)}
.prod-card{position:absolute;top:1707px;width:217px;height:289px;background:var(--white);border-radius:6px;overflow:hidden}
.prod-card .photo{height:138px}
.prod-card h3{position:absolute;left:18px;top:154px;font-size:13px;font-weight:600;line-height:18px}
.prod-card p{position:absolute;left:18px;top:185px;width:182px;font-size:9px;line-height:16px;color:#444}
.prod-card .share{position:absolute;right:26px;top:156px}
.foot-nav a{position:absolute;top:2125px;font-size:9px;font-weight:500;color:var(--white);text-decoration:none}
.foot-nav a.active{color:var(--green)}
.foot-h{font-size:13px;font-weight:600;color:var(--white)}
.foot-t{font-size:9px;line-height:16px;color:var(--white)}
.social{position:absolute;top:2208px;width:23px;height:23px;border-radius:50%;background:var(--white)}
</style>
</head>
<body>
<div class="page">

  <svg class="abs" style="left:0;top:0" width="997" height="360" viewBox="0 0 997 360">
    <path d="M0 0H997V194C930 270 800 320 660 300C540 282 470 250 380 280C250 320 120 330 0 352Z" fill="#eef4fa"/>
  </svg>

  <header>
    <div class="brand abs" style="left:162px;top:15px">VELMO</div>
    <nav class="nav">
      <a class="active" style="left:414px;top:26px">Home</a>
      <a style="left:461px;top:26px">About Us</a>
      <a style="left:529px;top:26px">Services</a>
      <a style="left:594px;top:26px">Testimonials</a>
      <a style="left:683px;top:26px">Contact Us</a>
    </nav>
    <div class="icon-btn" style="left:781px;top:20px">
      <svg width="10" height="10" viewBox="0 0 24 24"><path d="M6 2l4 4-2 3c1 3 4 6 7 7l3-2 4 4-3 4C10 21 3 14 2 5z" fill="#1e3a8f"/></svg>
    </div>
    <div class="icon-btn" style="left:812px;top:20px">
      <svg width="10" height="8" viewBox="0 0 20 14"><rect width="20" height="14" rx="1" fill="#1e3a8f"/><path d="M1 1l9 7 9-7" stroke="#fff" stroke-width="1.6" fill="none"/></svg>
    </div>
  </header>

  <section class="hero">
    <div class="photo ph-infusion abs" role="img" aria-label="Patient relaxing in a clinic chair during an IV drip" style="left:160px;top:80px;width:301px;height:301px;border-radius:50%"></div>
    <p class="abs" style="left:505px;top:112px;font-size:12.5px;font-weight:500;color:var(--navy);line-height:16px">"Revitalize Your Body With</p>
    <h1 class="abs" style="left:505px;top:128px;font-size:26px;font-weight:700;color:var(--ink);white-space:nowrap;line-height:32px">IV NUTRIENT THERAPY"</h1>
    <p class="abs" style="left:505px;top:166px;width:340px;font-size:9px;line-height:14px">Short benefit-driven statement, e.g., "Boost immunity, hydrate instantly, and increase energy with our custom IV drips."</p>
    <div class="btn" style="left:505px;top:209px;width:119px;height:26px">EXPLORE SERVICES</div>
  </section>

  <section class="about">
    <h2 class="section-title abs" style="left:161px;top:446px">WHO WE ARE VELMO</h2>
    <div class="rule" style="left:161px;top:478px"><i></i><i></i></div>
    <p class="abs" style="left:161px;top:500px;width:292px;font-size:9px;line-height:14px">Lorem ipsum dolor sit amet, consectetuer adipiscing elit, sed diam nonummy nibh euismod tincidunt ut laoreet dolore magna aliquam erat volutpat. Ut wisi enim ad minim veniam, quis nostrud exerci tation ullamcorper suscipit.</p>
    <div class="btn" style="left:161px;top:577px;width:95px;height:27px">CONTACT US</div>
    <div class="photo ph-patient abs" role="img" aria-label="Smiling patient holding an IV line" style="left:498px;top:391px;width:158px;height:283px;border-radius:79px"></div>
    <div class="photo ph-nurse abs" role="img" aria-label="Nurse preparing a blood sample tube" style="left:677px;top:439px;width:158px;height:283px;border-radius:79px"></div>
  </section>

  <section class="services">
    <div class="band" style="top:756px;height:332px"></div>
    <h2 class="section-title abs" style="left:0;width:997px;text-align:center;top:789px">OUR SERVICES</h2>
    <div class="rule" style="left:461px;top:820px"><i></i><i></i></div>
    <div class="arrow" style="left:121px;top:940px"><svg width="8" height="8" viewBox="0 0 10 10"><path d="M7 1L3 5l4 4" stroke="#8ab453" stroke-width="1.6" fill="none"/></svg></div>
    <div class="arrow" style="left:857px;top:940px"><svg width="8" height="8" viewBox="0 0 10 10"><path d="M3 1l4 4-4 4" stroke="#8ab453" stroke-width="1.6" fill="none"/></svg></div>
    <article class="svc-card" style="left:160px">
      <div class="photo ph-consult" role="img" aria-label="Nurse reviewing a treatment plan with a client"></div>
      <svg class="glyph" viewBox="0 0 40 40"><path d="M20 5l12 5v9c0 8-5 13-12 16C13 32 8 27 8 19v-9z" stroke="#1f8fd6" stroke-width="2" fill="none"/><path d="M15 20l4 4 7-8" stroke="#1f8fd6" stroke-width="2" fill="none"/></svg>
      <h3>Immunity Boost<br>IV Drip:</h3>
    </article>
    <article class="svc-card" style="left:390px">
      <div class="photo ph-cannula" role="img" aria-label="Gloved hands placing an IV cannula"></div>
      <svg class="glyph" viewBox="0 0 40 40"><path d="M20 5c6 9 10 14 10 20a10 10 0 01-20 0c0-6 4-11 10-20z" stroke="#1f8fd6" stroke-width="2" fill="none"/><path d="M15 26a5 5 0 005 5" stroke="#1f8fd6" stroke-width="2" fill="none"/></svg>
      <h3>Hydration<br>Therapy:</h3>
    </article>
    <article class="svc-card" style="left:619px">
      <div class="photo ph-arm" role="img" aria-label="Clinician preparing a patient's arm for an infusion"></div>
      <svg class="glyph" viewBox="0 0 40 40"><path d="M23 4L10 23h9l-2 13 13-19h-9z" stroke="#1f8fd6" stroke-width="2" fill="none" stroke-linejoin="round"/></svg>
      <h3 style="top:162px">Energy Recharge:</h3>
    </article>
  </section>

  <section class="testimonials">
    <div class="abs" style="left:-29px;top:1332px;width:220px;height:220px;border-radius:50%;background:var(--mist)"></div>
    <div class="abs" style="left:201px;top:1498px;width:77px;height:77px;border-radius:50%;background:var(--mist)"></div>
    <h2 class="section-title abs" style="left:161px;top:1219px">CLIENT TESTIMONIAL</h2>
    <div class="rule" style="left:161px;top:1250px"><i></i><i></i></div>
    <div class="review">
      <div class="photo ph-avatar abs" role="img" aria-label="Reviewer portrait" style="left:24px;top:16px;width:49px;height:49px;border-radius:50%"></div>
      <p class="abs" style="left:89px;top:18px;font-size:9.5px;font-weight:500;line-height:13px">Jonah Reyes</p>
      <p class="abs" style="left:90px;top:33px;font-size:7px;line-height:10px">Lorem Ipsum</p>
      <p class="abs" style="left:89px;top:44px;font-size:8px;color:#f2c200;letter-spacing:1px;line-height:10px">★★★★★</p>
      <p class="abs" style="left:24px;top:76px;width:268px;font-size:10px;line-height:16px;color:var(--muted)">Lorem ipsum dolor sit amet, consectetuer adipiscing elit, sed diam nonummy nibh euismod tincidunt ut laoreet dolore magna aliquam erat volutpat. Ut wisi enim ad</p>
      <svg class="abs" style="left:259px;top:151px" width="38" height="10" viewBox="0 0 38 10"><path d="M12 5H1M5 1L1 5l4 4M26 5h11M33 1l4 4-4 4" stroke="#2b2b2b" stroke-width="1.2" fill="none"/></svg>
    </div>
    <div class="photo ph-portrait-a abs" role="img" aria-label="Portrait of a client in a turtleneck" style="left:491px;top:1186px;width:188px;height:188px;border-radius:50%"></div>
    <div class="photo ph-portrait-b abs" role="img" aria-label="Portrait of a smiling client in a plaid shirt" style="left:696px;top:1279px;width:154px;height:154px;border-radius:50%"></div>
    <div class="photo ph-portrait-c abs" role="img" aria-label="Portrait of a client in a dark blazer" style="left:547px;top:1412px;width:188px;height:188px;border-radius:50%"></div>
  </section>

  <section class="products">
    <div class="band" style="top:1623px;height:420px"></div>
    <h2 class="section-title abs" style="left:0;width:997px;text-align:center;top:1649px">OUR PRODUCTS</h2>
    <div class="rule" style="left:461px;top:1680px"><i></i><i></i></div>
    <article class="prod-card" style="left:160px">
      <div class="photo ph-consult" role="img" aria-label="Nurse reviewing a treatment plan with a client"></div>
      <h3>Join the family</h3>
      <svg class="share" width="13" height="14" viewBox="0 0 13 14"><circle cx="10" cy="2.5" r="2.3" fill="#1e3a8f"/><circle cx="2.5" cy="7" r="2.3" fill="#1e3a8f"/><circle cx="10" cy="11.5" r="2.3" fill="#1e3a8f"/><path d="M10 2.5L2.5 7 10 11.5" stroke="#1e3a8f" stroke-width="1.3" fill="none"/></svg>
      <p>Our membership plan gives you monthly IV sessions, priority booking and a personal nurse who tailors every vitamin blend to your health goals and lifestyle.</p>
    </article>
    <article class="prod-card" style="left:389px">
      <div class="photo ph-cannula" role="img" aria-label="Gloved hands placing an IV cannula"></div>
      <h3>We get to work</h3>
      <svg class="share" width="13" height="14" viewBox="0 0 13 14"><circle cx="10" cy="2.5" r="2.3" fill="#1e3a8f"/><circle cx="2.5" cy="7" r="2.3" fill="#1e3a8f"/><circle cx="10" cy="11.5" r="2.3" fill="#1e3a8f"/><path d="M10 2.5L2.5 7 10 11.5" stroke="#1e3a8f" stroke-width="1.3" fill="none"/></svg>
      <p>Our licensed nurses place your line gently and monitor every drip, delivering fluids, vitamins and minerals straight to your bloodstream for fast, full absorption and comfort.</p>
    </article>
    <article class="prod-card" style="left:618px">
      <div class="photo ph-arm" role="img" aria-label="Clinician preparing a patient's arm for an infusion"></div>
      <h3>Enjoy the goods</h3>
      <svg class="share" width="13" height="14" viewBox="0 0 13 14"><circle cx="10" cy="2.5" r="2.3" fill="#1e3a8f"/><circle cx="2.5" cy="7" r="2.3" fill="#1e3a8f"/><circle cx="10" cy="11.5" r="2.3" fill="#1e3a8f"/><path d="M10 2.5L2.5 7 10 11.5" stroke="#1e3a8f" stroke-width="1.3" fill="none"/></svg>
      <p>Walk out refreshed with brighter skin, steadier energy and stronger immunity. Most clients feel the difference within hours, and the benefits last for days after each session.</p>
    </article>
  </section>

  <footer>
    <svg class="abs" style="left:0;top:1980px" width="997" height="324" viewBox="0 0 997 324">
      <path d="M0 172C90 90 200 40 330 44C450 48 530 100 640 100C800 100 900 70 997 9V324H0Z" fill="#1e3a8f"/>
    </svg>
    <div class="brand abs" style="left:162px;top:2112px;color:var(--white);font-size:28px">VELMO</div>
    <nav class="foot-nav">
      <a class="active" style="left:459px">Home</a>
      <a style="left:513px">About</a>
      <a style="left:568px">Treatments</a>
      <a style="left:650px">Testimonials</a>
      <a style="left:736px">Blog</a>
      <a style="left:783px">Contact Us</a>
    </nav>
    <div class="abs" style="left:146px;top:2187px;width:703px;height:1px;background:rgba(255,255,255,.35)"></div>
    <svg class="abs" style="left:161px;top:2216px" width="11" height="13" viewBox="0 0 11 13"><path d="M5.5 12S1 7.5 1 4.8a4.5 4.5 0 019 0C10 7.5 5.5 12 5.5 12z" stroke="#fff" stroke-width="1.1" fill="none"/><circle cx="5.5" cy="4.8" r="1.5" stroke="#fff" stroke-width="1" fill="none"/></svg>
    <p class="foot-h abs" style="left:180px;top:2211px">ADDRESS</p>
    <p class="foot-t abs" style="left:180px;top:2233px">Marlow Avenue<br>Fenwick, Texas</p>
    <svg class="abs" style="left:388px;top:2216px" width="12" height="12" viewBox="0 0 24 24"><path d="M6 2l4 4-2 3c1 3 4 6 7 7l3-2 4 4-3 4C10 21 3 14 2 5z" stroke="#fff" stroke-width="1.8" fill="none"/></svg>
    <p class="foot-h abs" style="left:410px;top:2211px">PHONE</p>
    <p class="foot-t abs" style="left:409px;top:2230px">Call: (555)201-4477<br>Email:hello@velmoclinic.example</p>
    <div class="social" role="img" aria-label="Social link" style="left:749px"></div>
    <div class="social" role="img" aria-label="Social link" style="left:781px"></div>
    <div class="social" role="img" aria-label="Social link" style="left:812px"></div>
    <p class="abs" style="left:0;width:997px;text-align:center;top:2280px;font-size:7px;color:var(--white)">Copyright © 2024 Harlow Crest Partners, LLC All rights reserved</p>
  </footer>

</div>
</body>
</html>
```